Kickgrid Numbers Service

We have a football stats service that we feel would benefit from some design input. In particular we would like the designer to look at three pages. We will then transfer this style across the rest of the site.

We are looking for designs for three pages. Links to the existing pages we would like reworked are:

Player:
http://demostats.kickgrid-example.com/Player.asp?lang=&coid=4&teid=220&plid=197404

Team Stats:
http://demostats.kickgrid-example.com/Team_Stats.asp?lang=&coid=4&teid=218

League Table:
http://demostats.kickgrid-example.com/Comp_Table.asp?lang=&coid=4

We require the page structure to remain as is with the main country/competition selector on the left and the content on the right.

The colour palette, fonts, content separators etc are all in your hands. We will use this version as a sales tool for our services. In many cases this will be restyled to match a specific clients requirements.

We are happy for this to be done in HTML/CSS or as a layered image file.

Target Market(s)

These stats pages are for use on newspaper and bookmaker websites.

Industry/Entity Type

Sales

Requirements
Nice to have
• A nice colour palette for graphs and charts is important.

```html
<!DOCTYPE html>
<html lang="en">
<head>
<meta charset="utf-8">
<title>Kickgrid Numbers – Player</title>
<link href="https://fonts.googleapis.com/css2?family=Open+Sans:wght@400;600;700&display=swap" rel="stylesheet">
<style>
:root{
  --page:#ffffff;
  --screen-bg:#e9eaec;
  --card:#ffffff;
  --ink:#333333;
  --ink-soft:#555555;
  --rule:#dddddd;
  --side:#23262d;
  --side-ink:#ffffff;
  --side-muted:#8a8d93;
  --accent:#428bca;
  --photo-a:#6f7f8c;
  --photo-b:#c9a48a;
}
*{box-sizing:border-box;margin:0;padding:0}
html,body{width:1200px;height:838px;overflow:hidden;background:var(--page);font-family:"Open Sans",Arial,sans-serif;color:var(--ink)}
.stage{position:relative;width:1200px;height:838px}
.screen{position:absolute;top:100px;width:354px;height:650px;background:var(--screen-bg);overflow:hidden;border:1px solid #ccc}
.screen--profile{left:71px}
.screen--menu{left:772px}
.topbar{position:absolute;left:0;top:0;right:0;height:52px;background:var(--card);border-bottom:1px solid var(--rule);z-index:3}
.topbar__toggle{position:absolute;left:0;top:0;width:52px;height:52px;border-right:1px solid var(--rule);display:flex;align-items:center;justify-content:center}
.screen--menu .topbar__toggle{width:55px;background:#f4f4f4}
.topbar__brand{position:absolute;top:15px;left:73px;font-size:17px;font-weight:600;line-height:22px;color:var(--ink)}
.screen--menu .topbar__brand{left:85px}
.topbar__user{position:absolute;top:9px;left:267px;width:34px;height:34px;border-radius:50%;background:radial-gradient(circle at 50% 40%,#8a8a8a,#2b2b2b)}
.topbar__caret{position:absolute;top:24px;left:306px;width:0;height:0;border-left:4px solid transparent;border-right:4px solid transparent;border-top:5px solid var(--ink)}
.card{position:absolute;left:12px;top:71px;width:321px;height:600px;background:var(--card);border-radius:3px}
.card__photo{position:absolute;left:87px;top:15px;width:147px;height:147px;border-radius:50%;background:radial-gradient(circle at 50% 45%,var(--photo-b),var(--photo-a))}
.card__name{position:absolute;top:174px;left:0;right:0;text-align:center;font-size:27px;line-height:34px;font-weight:400;color:#444;white-space:nowrap}
.card__club{position:absolute;top:216px;left:0;right:0;height:24px;text-align:center;font-size:19px;line-height:24px;color:var(--ink-soft);display:flex;justify-content:center;align-items:center;gap:6px}
.card__facts{position:absolute;top:251px;left:0;right:0;text-align:center;font-size:14px;line-height:21px}
.card__facts b{font-weight:700}
.card__rule{position:absolute;top:338px;left:0;right:0;border-top:1px solid var(--rule)}
.stat{position:absolute;left:35px;font-size:14px;line-height:20px;white-space:nowrap}
.stat__label{font-weight:700}
.stat__value{display:flex;align-items:center;gap:4px}
.side{position:absolute;left:0;top:52px;width:272px;bottom:0;background:var(--side);color:var(--side-ink);z-index:2}
.side__date{position:absolute;left:20px;top:30px;font-size:17px;line-height:22px;display:flex;align-items:center;gap:10px}
.side__label{position:absolute;left:20px;font-size:13px;line-height:18px;font-weight:600;color:var(--side-muted)}
.side__search{position:absolute;left:11px;top:111px;width:247px;height:27px;background:#fff;border-radius:14px;font-size:11px;color:#999;padding:6px 12px;display:flex;justify-content:space-between;align-items:center}
.side__group{position:absolute;left:9px;top:206px;width:252px;height:41px;background:var(--accent);border-radius:3px;font-size:14px;padding:11px 11px;display:flex;justify-content:space-between;align-items:center}
.side__item{position:absolute;left:34px;width:216px;font-size:14px;line-height:20px;display:flex;align-items:center;justify-content:space-between}
.side__item span{display:flex;align-items:center;gap:9px}
.side__more{position:absolute;left:20px;top:504px;width:230px;font-size:14px;line-height:20px;display:flex;justify-content:space-between;align-items:center}
.peek{position:absolute;left:289px;top:84px;width:321px;height:600px;background:var(--card);border-radius:3px}
.peek__name{position:absolute;top:177px;left:54px;font-size:27px;line-height:34px;color:#444;white-space:nowrap}
.peek .card__rule{top:343px}
.note{position:absolute;left:541px;top:175px;font-size:22px;line-height:30px;font-weight:700;color:#000}
.note-arrow{position:absolute;left:670px;top:125px}
</style>
</head>
<body>
<div class="stage">

  <section class="screen screen--profile">
    <header class="topbar">
      <div class="topbar__toggle"><svg width="18" height="14"><rect y="0" width="18" height="2" fill="#333"/><rect y="6" width="18" height="2" fill="#333"/><rect y="12" width="18" height="2" fill="#333"/></svg></div>
      <div class="topbar__brand">Kickgrid Numbers</div>
      <div class="topbar__user" role="img" aria-label="User avatar photo"></div>
      <div class="topbar__caret"></div>
    </header>
    <article class="card">
      <div class="card__photo" role="img" aria-label="Player portrait photo"></div>
      <h1 class="card__name">Darko Milanovic</h1>
      <div class="card__club"><svg width="26" height="16"><rect width="26" height="16" fill="#fff" stroke="#ccc"/><rect x="10.5" width="5" height="16" fill="#d22"/><rect y="5.5" width="26" height="5" fill="#d22"/></svg>Riverside FC</div>
      <div class="card__facts">
        <div><b>Position:</b> Defender</div>
        <div><b>Date of Birth:</b> 22/02/1984</div>
        <div><b>Age:</b> 30</div>
      </div>
      <div class="card__rule"></div>
      <div class="stat" style="top:358px"><div class="stat__label">Height</div><div>1.88 m / 6 ft 2 in</div></div>
      <div class="stat" style="top:421px"><div class="stat__label">Weight</div><div>86 kg /13 st 8 lbs</div></div>
      <div class="stat" style="top:470px"><div class="stat__label">Place of Birth</div><div>Sremska Mitrovica, Serbia</div></div>
      <div class="stat" style="top:526px"><div class="stat__label">Nationality</div><div class="stat__value"><svg width="28" height="14"><rect width="28" height="5" fill="#c6363c"/><rect y="5" width="28" height="4" fill="#0c4076"/><rect y="9" width="28" height="5" fill="#fff"/></svg>Serbia</div></div>
    </article>
  </section>

  <div class="note">On menu click</div>
  <svg class="note-arrow" width="84" height="50"><path d="M4 46 C20 20 45 14 76 10" fill="none" stroke="#000" stroke-width="2"/><path d="M66 4 L78 10 L67 17" fill="none" stroke="#000" stroke-width="2"/></svg>

  <section class="screen screen--menu">
    <header class="topbar">
      <div class="topbar__toggle"><svg width="18" height="14"><rect y="0" width="18" height="2" fill="#333"/><rect y="6" width="18" height="2" fill="#333"/><rect y="12" width="18" height="2" fill="#333"/></svg></div>
      <div class="topbar__brand">Kickgrid Numbers</div>
      <div class="topbar__user" role="img" aria-label="User avatar photo"></div>
      <div class="topbar__caret"></div>
    </header>
    <div class="peek">
      <div class="peek__name">Darko Milanovic</div>
      <div class="card__rule"></div>
      <div class="stat" style="top:363px"><div class="stat__label">Height</div><div>1.88 m / 6 ft 2 in</div></div>
      <div class="stat" style="top:426px"><div class="stat__label">Weight</div><div>86 kg /13 st 8 lbs</div></div>
      <div class="stat" style="top:475px"><div class="stat__label">Place of Birth</div><div>Sremska Mitrovica, Serbia</div></div>
      <div class="stat" style="top:531px"><div class="stat__label">Nationality</div><div class="stat__value"><svg width="28" height="14"><rect width="28" height="5" fill="#c6363c"/><rect y="5" width="28" height="4" fill="#0c4076"/><rect y="9" width="28" height="5" fill="#fff"/></svg>Serbia</div></div>
    </div>
    <nav class="side">
      <div class="side__date"><svg width="18" height="18"><rect x="1" y="3" width="16" height="14" fill="none" stroke="#fff" stroke-width="2"/><rect x="1" y="3" width="16" height="4" fill="#fff"/><path d="M5 1v4M13 1v4M1 11h16M7 7v10M11 7v10" stroke="#fff" stroke-width="1.5"/></svg>25 September 2014</div>
      <div class="side__label" style="top:88px">Search</div>
      <div class="side__search">Search ...<svg width="12" height="12"><circle cx="5" cy="5" r="3.8" fill="none" stroke="#333" stroke-width="1.8"/><path d="M8 8l3 3" stroke="#333" stroke-width="2"/></svg></div>
      <div class="side__label" style="top:184px">Domestic Football</div>
      <div class="side__group">Domestic Football<svg width="12" height="8"><path d="M2 2l4 4 4-4" fill="none" stroke="#fff" stroke-width="2"/></svg></div>
      <div class="side__item" style="top:258px"><span><svg width="5" height="8"><path d="M0 0l5 4-5 4z" fill="#fff"/></svg>England</span><svg width="30" height="17"><rect width="30" height="17" fill="#fff"/><rect x="12.5" width="5" height="17" fill="#d22"/><rect y="6" width="30" height="5" fill="#d22"/></svg></div>
      <div class="side__item" style="top:295px"><span><svg width="5" height="8"><path d="M0 0l5 4-5 4z" fill="#fff"/></svg>Scotland</span><svg width="30" height="17"><rect width="30" height="17" fill="#0065bd"/><path d="M0 0L30 17M30 0L0 17" stroke="#fff" stroke-width="3"/></svg></div>
      <div class="side__item" style="top:332px"><span><svg width="5" height="8"><path d="M0 0l5 4-5 4z" fill="#fff"/></svg>Spain</span><svg width="30" height="17"><rect width="30" height="17" fill="#c60b1e"/><rect y="4.5" width="30" height="8" fill="#ffc400"/></svg></div>
      <div class="side__item" style="top:369px"><span><svg width="5" height="8"><path d="M0 0l5 4-5 4z" fill="#fff"/></svg>Italy</span><svg width="30" height="17"><rect width="10" height="17" fill="#009246"/><rect x="10" width="10" height="17" fill="#fff"/><rect x="20" width="10" height="17" fill="#ce2b37"/></svg></div>
      <div class="side__item" style="top:407px"><span><svg width="5" height="8"><path d="M0 0l5 4-5 4z" fill="#fff"/></svg>Germany</span><svg width="30" height="17"><rect width="30" height="6" fill="#000"/><rect y="6" width="30" height="5" fill="#dd0000"/><rect y="11" width="30" height="6" fill="#ffce00"/></svg></div>
      <div class="side__item" style="top:443px"><span><svg width="5" height="8"><path d="M0 0l5 4-5 4z" fill="#fff"/></svg>France</span><svg width="30" height="17"><rect width="10" height="17" fill="#0055a4"/><rect x="10" width="10" height="17" fill="#fff"/><rect x="20" width="10" height="17" fill="#ef4135"/></svg></div>
      <div class="side__more">Continental Football<svg width="8" height="12"><path d="M2 2l4 4-4 4" fill="none" stroke="#fff" stroke-width="2"/></svg></div>
    </nav>
  </section>

</div>
</body>
</html>
```